Landing Page / Waitlist

I would like a landing page for people to sign up for a waiting list. The text on the page should include (but is not limited to):
1) Main point: The accounting system you'll love
2) Secondary points:
a. Ruthlessly efficient
b. Quietly intelligent
c. Driven by AI
I've attached a file of our logo

The design should be simple, clean, and innovative - this is an ai company

```html
<!DOCTYPE html>
<html lang="en">
<head>
<meta charset="UTF-8">
<title>Tally North — Join the Waitlist</title>
<link rel="stylesheet" href="https://fonts.googleapis.com/css2?family=Montserrat:wght@600;700&family=Lato:wght@400&display=swap">
<style>
  :root {
    --navy-deep: #061526;
    --navy: #0b2338;
    --teal-haze: #123f52;
    --white: #ffffff;
    --text-soft: #eef3f8;
    --accent: #0996fb;
    --rule: rgba(255, 255, 255, 0.85);
  }
  * { box-sizing: border-box; margin: 0; padding: 0; }
  html, body {
    width: 1200px;
    height: 600px;
    overflow: hidden;
    background: var(--navy-deep);
  }
  .landing {
    position: relative;
    width: 1200px;
    height: 600px;
    overflow: hidden;
    font-family: 'Lato', Arial, sans-serif;
    color: var(--white);
  }
  .backdrop {
    position: absolute;
    inset: 0;
    background:
      radial-gradient(ellipse 420px 260px at 720px 300px, rgba(40, 80, 105, 0.55), transparent 70%),
      radial-gradient(ellipse 700px 220px at 600px 600px, rgba(22, 90, 105, 0.55), transparent 75%),
      linear-gradient(180deg, var(--navy-deep) 0%, var(--navy) 55%, var(--teal-haze) 100%);
  }
  .brand-panel {
    position: absolute;
    left: 0;
    top: 0;
    width: 517px;
    height: 600px;
    display: flex;
    flex-direction: column;
    align-items: center;
    justify-content: center;
    padding-top: 30px;
  }
  .wordmark {
    display: flex;
    align-items: center;
    gap: 14px;
    font-family: 'Montserrat', Arial, sans-serif;
    font-weight: 600;
    font-size: 46px;
    letter-spacing: -0.5px;
    color: var(--white);
  }
  .wordmark-square {
    width: 30px;
    height: 30px;
    background: var(--accent);
  }
  .copyright {
    margin-top: 34px;
    font-size: 15px;
    color: var(--text-soft);
  }
  .divider {
    position: absolute;
    left: 517px;
    top: 87px;
    width: 1px;
    height: 426px;
    background: var(--rule);
  }
  .waitlist-panel {
    position: absolute;
    left: 627px;
    top: 176px;
    width: 500px;
  }
  .headline {
    font-family: 'Montserrat', Arial, sans-serif;
    font-weight: 700;
    font-size: 38px;
    line-height: 49px;
    color: var(--white);
  }
  .tagline {
    margin-top: 22px;
    font-size: 21px;
    color: var(--text-soft);
    margin-left: -2px;
  }
  .signup {
    margin-top: 24px;
    width: 486px;
    height: 60px;
    border: 1px solid var(--rule);
    border-radius: 30px;
    display: flex;
    align-items: center;
    justify-content: space-between;
    padding: 0 4px 0 30px;
  }
  .signup-email {
    flex: 1;
    background: transparent;
    border: none;
    outline: none;
    font-family: 'Lato', Arial, sans-serif;
    font-size: 18px;
    color: var(--white);
  }
  .signup-email::placeholder { color: var(--white); opacity: 1; }
  .signup-button {
    width: 228px;
    height: 51px;
    border: none;
    border-radius: 26px;
    background: var(--accent);
    color: var(--white);
    font-family: 'Lato', Arial, sans-serif;
    font-size: 21px;
    cursor: pointer;
  }
</style>
</head>
<body>
  <main class="landing">
    <div class="backdrop" role="img" aria-label="Blurred city office towers overlaid with glowing financial line and bar charts"></div>

    <section class="brand-panel">
      <div class="wordmark">
        <span class="wordmark-square"></span>
        <span>TallyNorth</span>
      </div>
      <p class="copyright">Copyright © 2025 Tally North. All rights reserved.</p>
    </section>

    <div class="divider"></div>

    <section class="waitlist-panel">
      <h1 class="headline">The Accounting System<br>You'll Love</h1>
      <p class="tagline">Ruthlessly efficient. Quietly intelligent. Driven by AI.</p>
      <form class="signup">
        <input class="signup-email" type="email" placeholder="Email" aria-label="Email">
        <button class="signup-button" type="button">Join the Waitlist</button>
      </form>
    </section>
  </main>
</body>
</html>
```